Belvanta - Awnings & Outdoor Blinds

We need a brochure design for out Australia based Awnings & Outdoor Blinds company.

We require 2 templates:

1. Product Specific. (For One Product) - Single or Double Sided A4
Must Include:
Our Logo, Product Description, Pictures,Product Features & Benefits (in point form) & Our Contact Details (Phone & Website).

2.Product Range (Our Full Range) - 8 Page A4 (2x A3 Folded In Half Printed Both Sides).
Must Include:
Page 1 - Front Cover - Title (Product Range) Cover With Our Logo & Photo/s.
Page 2 - About Us, Why Us & Warranty Information.
Page 3 - A Gallery (Just Photos Showcasing Our Work)
Page 4 - 3 Products Per Page (Image/s, Product Title & Brief Description).
Page 5 - 3 Products Per Page (Image/s, Product Title & Brief Description).
Page 6 - 3 Products Per Page (Image/s, Product Title & Brief Description).
Page 7 - 3 Products Per Page (Image/s, Product Title & Brief Description).
Page 8 - Back Cover with our Contact Details (Phone, Website & Logo).

We are just looking for templates we will fill in all the content, needs to be easy to customise (change photos/text etc).

For more info on what we do: http://site7305.example-builder.com/belvanta

Requirements
Nice to have
• Nice to have the product pages 4 - 7 not as identical layout.

Nice to be in our colours Red, White, Black, Light Grey. (See Logo Variations - Logo is the top one).

```html
<!DOCTYPE html>
<html lang="en">
<head>
<meta charset="utf-8">
<title>Belvanta – Folding Arm Awnings Product Sheet</title>
<link href="https://fonts.googleapis.com/css2?family=Open+Sans:wght@400;600;700&display=swap" rel="stylesheet">
<style>
  :root{
    --red:#c0213a;
    --red-dark:#a51a31;
    --grey:#cfcfcf;
    --grey-dark:#b3b3b3;
    --grey-light:#e4e4e4;
    --grey-text:#9a9a9a;
    --ink:#222;
    --white:#fff;
    --pink-text:#f1b8c1;
    --board:#fff;
  }
  *{box-sizing:border-box;margin:0;padding:0}
  html,body{width:803px;height:1200px;overflow:hidden;background:var(--board)}
  body{font-family:"Open Sans",Arial,sans-serif;color:var(--ink)}
  .board{position:absolute;left:0;top:0;width:735px;height:1100px;transform:scale(1.09);transform-origin:0 0}
  .board > *{position:absolute}
  .option-title{font-size:13px;font-weight:600;letter-spacing:.2px}
  .side-label{font-size:10px;font-weight:600}

  .page{width:333px;height:469px;background:var(--white);box-shadow:2px 3px 5px rgba(0,0,0,.35);overflow:hidden}
  .page > *{position:absolute}

  .photo{display:block}
  .photo--awning{background:linear-gradient(165deg,#93b9dc 0%,#b43a32 30%,#a89278 55%,#5f564c 100%)}
  .photo--pool{background:linear-gradient(175deg,#a9c8e0 0%,#d9d6cf 45%,#4fa3c8 100%)}
  .photo--dark{background:linear-gradient(170deg,#7da5c6 0%,#5d6a6d 45%,#3b3a37 100%)}
  .photo--stone{background:linear-gradient(170deg,#9ebfdc 0%,#d0c7b8 40%,#8d8577 75%,#6c9a56 100%)}
  .photo--white{background:linear-gradient(170deg,#c9d6df 0%,#e9e6e0 50%,#b9b1a5 100%)}

  /* front */
  .front__corner{left:0;top:0;width:85px;height:47px}
  .front__title{left:94px;top:0;width:239px;height:47px;display:flex;align-items:center;justify-content:center;color:var(--white);font-size:13px;font-weight:600;letter-spacing:.3px;background:var(--grey)}
  .front__hero{left:0;top:50px;width:333px;height:147px}
  .front__thumb-panel{left:88px;top:137px;width:245px;height:60px;background:var(--red)}
  .front__band{left:0;top:197px;width:333px;height:175px;background:var(--red)}
  .front__thumb{top:144px;width:72px;height:76px}
  .front__intro{left:20px;top:232px;width:305px;font-size:6.4px;line-height:1.45;text-transform:uppercase;color:var(--pink-text)}
  .front__lower-photo{left:0;top:289px;width:161px;height:83px}
  .features{left:169px;top:284px;width:158px;color:var(--white)}
  .features__heading{font-size:8.5px;font-weight:600;margin-bottom:3px}
  .features__list{list-style:none;font-size:5px;line-height:1.4}
  .features__list li{position:relative;padding-left:6px;margin-bottom:5px}
  .features__list li::before{content:"•";position:absolute;left:0}
  .front__url{left:20px;top:438px;font-size:6px;letter-spacing:.6px;color:var(--grey-text)}

  .brand{display:flex;align-items:center;gap:5px}
  .brand__mark{border-radius:50%;background:var(--red);flex:none}
  .brand__name{font-weight:600;color:var(--ink);line-height:1;white-space:nowrap}
  .brand__tag{color:var(--grey-text);margin-top:3px;white-space:nowrap}
  .front__brand{left:136px;top:402px}
  .front__brand .brand__mark{width:32px;height:32px}
  .front__brand .brand__name{font-size:16px}
  .front__brand .brand__tag{font-size:4.4px;letter-spacing:1.1px}

  /* back */
  .back__strip{left:0;top:0;width:40px;height:283px;background:var(--grey)}
  .back__tall{left:40px;top:75px;width:70px;height:208px}
  .back__top{left:114px;top:0;width:220px;height:112px}
  .back__fill{left:258px;top:190px;width:76px;height:93px;background:var(--grey-light)}
  .back__tile{top:117px;height:73px}
  .back__tile--grey{background:var(--grey)}
  .back__wide{left:114px;top:195px;width:144px;height:88px}
  .back__band{left:0;top:283px;width:334px;height:100px;background:var(--red)}
  .back__band-side{left:0;top:283px;width:114px;height:100px;background:var(--red-dark)}
  .specs{left:114px;top:296px;width:210px;color:var(--white)}
  .specs__heading{font-size:8px;font-weight:700;line-height:1.2}
  .specs__text{font-size:5.2px;line-height:1.45;margin:1px 0 6px;padding-left:6px;position:relative}
  .specs__text::before{content:"•";position:absolute;left:0}
  .contact{left:22px;top:393px;font-size:5.2px;line-height:1.5;color:var(--grey-text)}
  .contact strong{font-weight:700}
  .hours{left:22px;top:444px;font-size:5.2px;color:var(--grey-text)}
  .back__brand{left:183px;top:414px}
  .back__brand .brand__mark{width:24px;height:24px}
  .back__brand .brand__name{font-size:12px}
  .back__brand .brand__tag{font-size:3.4px;letter-spacing:.8px;margin-top:2px}

  /* option 2 colourway */
  .page--red .front__title{background:var(--red)}
  .page--red .front__band{background:var(--grey)}
  .page--red .front__intro{color:var(--grey-text)}
  .page--red .features{color:var(--grey-text)}
  .page--red .features__heading{color:var(--red)}
  .page--red .back__strip{background:var(--red)}
  .page--red .back__band{background:var(--grey-light)}
  .page--red .back__band-side{background:var(--grey-dark)}
  .page--red .specs{color:var(--grey-text)}
  .page--red .specs__heading{color:var(--red)}
</style>
</head>
<body>
<main class="board">

  <h2 class="option-title" style="left:26px;top:12px">PRODUCT SHEET OPTION 1</h2>
  <span class="side-label" style="left:26px;top:48px">FRONT</span>
  <span class="side-label" style="left:373px;top:48px">BACK</span>

  <section class="page page--grey" style="left:24px;top:68px">
    <div class="photo photo--white front__corner" role="img" aria-label="Close-up of awning against stone wall"></div>
    <h1 class="front__title">FOLDING ARM AWNINGS</h1>
    <div class="photo photo--awning front__hero" role="img" aria-label="Red folding arm awning over outdoor patio"></div>
    <div class="front__thumb-panel"></div>
    <div class="front__band"></div>
    <div class="photo photo--white front__thumb" style="left:95px" role="img" aria-label="Awning over deck"></div>
    <div class="photo photo--pool front__thumb" style="left:172px" role="img" aria-label="Awning beside pool"></div>
    <div class="photo photo--white front__thumb" style="left:249px;width:84px" role="img" aria-label="Awning fabric detail"></div>
    <p class="front__intro">Our folding arm awnings incorporate innovative new designs, reflecting today's demands for function, design and construction. These awnings are discreet, timeless designs that fit seamlessly in every setting, and can be neatly rolled away when not in use.</p>
    <div class="photo photo--pool front__lower-photo" role="img" aria-label="Poolside awning with yellow chairs"></div>
    <div class="features">
      <h3 class="features__heading">Features &amp; Benefits</h3>
      <ul class="features__list">
        <li>Durable fabrics: Many of the fabrics we use are manufactured in Australia to suit local conditions. Choose from sunscreen, acrylic or canvas fabrics knowing they will look great for many years.</li>
        <li>Technically superior materials: We make our Drop-Arm Fabric Awnings from components that have been engineered to last in Australia's harsh conditions.</li>
      </ul>
    </div>
    <div class="brand front__brand"><span class="brand__mark"></span><div><div class="brand__name">BelvantaDirect</div><div class="brand__tag">AWNINGS &amp; OUTDOOR BLINDS</div></div></div>
    <span class="front__url">WWW.BELVANTADIRECT.COM.AU</span>
  </section>

  <section class="page page--grey" style="left:370px;top:68px;width:334px">
    <div class="back__strip"></div>
    <div class="photo photo--pool back__tall" role="img" aria-label="Balcony awning over pool terrace"></div>
    <div class="photo photo--stone back__top" role="img" aria-label="Modern home with patio awning"></div>
    <div class="back__fill"></div>
    <div class="photo photo--pool back__tile" style="left:114px;width:69px" role="img" aria-label="Awning over ocean view deck"></div>
    <div class="back__tile back__tile--grey" style="left:188px;width:68px"></div>
    <div class="photo photo--dark back__tile" style="left:261px;width:73px" role="img" aria-label="Grey awning on house"></div>
    <div class="photo photo--dark back__wide" role="img" aria-label="Awning over living room terrace"></div>
    <div class="back__band"></div>
    <div class="back__band-side"></div>
    <div class="specs">
      <h3 class="specs__heading">Operation</h3>
      <p class="specs__text">Crank Operated (Gearbox) as standard. Can also be motorised with optional Sun &amp; Wind sensor options.</p>
      <h3 class="specs__heading">Available Fabrics</h3>
      <p class="specs__text">Available in our Sunscreen &amp; Block Out fabrics.</p>
      <h3 class="specs__heading">Specifications</h3>
      <p class="specs__text">Maximum Width: 8000mm, Maximum Projection: 3500mm.</p>
    </div>
    <p class="contact">Unit 8 - 12 Harbour Rd,<br>Redbank QLD 4301<br>Phone: 1300 000 482<br>Email: info@belvanta.com.au<br><strong>WWW.BELVANTADIRECT.COM.AU</strong></p>
    <p class="hours">Trading Hours: Mon to Fri : 8am - 4pm</p>
    <div class="brand back__brand"><span class="brand__mark"></span><div><div class="brand__name">BelvantaDirect</div><div class="brand__tag">AWNINGS &amp; OUTDOOR BLINDS</div></div></div>
  </section>

  <h2 class="option-title" style="left:26px;top:577px">PRODUCT SHEET OPTION 2</h2>
  <span class="side-label" style="left:26px;top:600px">FRONT</span>
  <span class="side-label" style="left:381px;top:600px">BACK</span>

  <section class="page page--red" style="left:24px;top:619px">
    <div class="photo photo--white front__corner" role="img" aria-label="Close-up of awning against stone wall"></div>
    <h1 class="front__title">FOLDING ARM AWNINGS</h1>
    <div class="photo photo--awning front__hero" role="img" aria-label="Red folding arm awning over outdoor patio"></div>
    <div class="front__thumb-panel"></div>
    <div class="front__band"></div>
    <div class="photo photo--white front__thumb" style="left:95px" role="img" aria-label="Awning over deck"></div>
    <div class="photo photo--pool front__thumb" style="left:172px" role="img" aria-label="Awning beside pool"></div>
    <div class="photo photo--white front__thumb" style="left:249px;width:84px" role="img" aria-label="Awning fabric detail"></div>
    <p class="front__intro">Our folding arm awnings incorporate innovative new designs, reflecting today's demands for function, design and construction. These awnings are discreet, timeless designs that fit seamlessly in every setting, and can be neatly rolled away when not in use.</p>
    <div class="photo photo--pool front__lower-photo" role="img" aria-label="Poolside awning with yellow chairs"></div>
    <div class="features">
      <h3 class="features__heading">Features &amp; Benefits</h3>
      <ul class="features__list">
        <li>Durable fabrics: Many of the fabrics we use are manufactured in Australia to suit local conditions. Choose from sunscreen, acrylic or canvas fabrics knowing they will look great for many years.</li>
        <li>Technically superior materials: We make our Drop-Arm Fabric Awnings from components that have been engineered to last in Australia's harsh conditions.</li>
      </ul>
    </div>
    <div class="brand front__brand"><span class="brand__mark"></span><div><div class="brand__name">BelvantaDirect</div><div class="brand__tag">AWNINGS &amp; OUTDOOR BLINDS</div></div></div>
    <span class="front__url">WWW.BELVANTADIRECT.COM.AU</span>
  </section>

  <section class="page page--red" style="left:379px;top:619px;width:331px">
    <div class="back__strip"></div>
    <div class="photo photo--pool back__tall" role="img" aria-label="Balcony awning over pool terrace"></div>
    <div class="photo photo--stone back__top" style="width:217px" role="img" aria-label="Modern home with patio awning"></div>
    <div class="back__fill"></div>
    <div class="photo photo--pool back__tile" style="left:114px;width:69px" role="img" aria-label="Awning over ocean view deck"></div>
    <div class="back__tile back__tile--grey" style="left:188px;width:68px"></div>
    <div class="photo photo--dark back__tile" style="left:261px;width:70px" role="img" aria-label="Grey awning on house"></div>
    <div class="photo photo--dark back__wide" role="img" aria-label="Awning over living room terrace"></div>
    <div class="back__band"></div>
    <div class="back__band-side"></div>
    <div class="specs">
      <h3 class="specs__heading">Operation</h3>
      <p class="specs__text">Crank Operated (Gearbox) as standard. Can also be motorised with optional Sun &amp; Wind sensor options.</p>
      <h3 class="specs__heading">Available Fabrics</h3>
      <p class="specs__text">Available in our Sunscreen &amp; Block Out fabrics.</p>
      <h3 class="specs__heading">Specifications</h3>
      <p class="specs__text">Maximum Width: 8000mm, Maximum Projection: 3500mm.</p>
    </div>
    <p class="contact">Unit 8 - 12 Harbour Rd,<br>Redbank QLD 4301<br>Phone: 1300 000 482<br>Email: info@belvanta.com.au<br><strong>WWW.BELVANTADIRECT.COM.AU</strong></p>
    <p class="hours">Trading Hours: Mon to Fri : 8am - 4pm</p>
    <div class="brand back__brand"><span class="brand__mark"></span><div><div class="brand__name">BelvantaDirect</div><div class="brand__tag">AWNINGS &amp; OUTDOOR BLINDS</div></div></div>
  </section>

</main>
</body>
</html>
```